Business Card

Need a clean, professional, simple, but clever business card for our company LUMO RIDES. We only want to see black and white colors as that reflects the branding of our company. Attaching logo. Will also consider the "sky blue" shown in our web site sample png - but use of the color should be minimal.

Lumo Rides is a executive car service operating in cities throughout Africa. By operating well equipped Varento Halde vehicles, we offer the smoothest and stylish ride in town. We aim to provide customers with a valuable experience. That’s why we make sure our patrons get picked up like a boss, travel in style, and Arrive Polished.

We need a card that says that. Likely to print on the best quality/smoothest paper available, as it must speak volumes of our business and class.

We would like the rear of the card to be all black. Perhaps we can put the web url on it, or leave it blank if it looks neater/more elegant.

Use the following contact information (as you see fit):

Lumo Rides Limited
P.O. Box 58104
Dar es Salaam, Tanzania

Baraka Kilonzo
Managing Director

+255 (0) 712 904618
sales@lumorides.example

web url: www.lumorides.example
email: chauffeur@lumorides.example

***Winning designer will likely be commissioned for more promotional work in near future.

Target Market(s)

The target market for this card is corporate executives of top firms (financial, consulting, businessmen, etc). They are interested in high quality transportation. Our fleet is all high end Varento Halde black cars (black exterior, black interior); and therefore, that high end quality and promptness must be reflected in the card. Also simplicity, as we we take care of all the little details behind the scene.

Industry/Entity Type

Business

Requirements
Must have
• Font must be: Helvetica Neue, like the logo. You may use other variations (Thin, Ultra thin, Regular, Bold), so long as it looks and prints well.

If web url is included on the back of the card, then do NOT include it also on the front.
Nice to have
• If there is something nice and clever that you can do/think of that doesn't make the card look busy, but adds a little "posh", then I could be even more interested.

However, if there's no little thing do be done, I'd rather a simple, but very professional looking card that attracts a lot of attention.

```html
<!DOCTYPE html>
<html lang="en">
<head>
<meta charset="utf-8">
<title>Lumo Rides — Business Card</title>
<link rel="stylesheet" href="https://fonts.googleapis.com/css2?family=Inter:wght@300;400;600;700&display=swap">
<style>
  :root {
    --stage: #1b1b1c;
    --card-black: #232325;
    --band-black: #2a2b2d;
    --paper-white: #ffffff;
    --ink: #1e1e1e;
    --ink-soft: #5a5a5a;
    --silver: #d8d8d8;
    --silver-soft: #9a9a9a;
    --sky: #29b6d3;
  }
  * { box-sizing: border-box; margin: 0; padding: 0; }
  html, body {
    width: 1200px; height: 1000px; overflow: hidden;
    background: var(--stage);
    font-family: "Inter", "Helvetica Neue", Arial, sans-serif;
  }
  .canvas { position: relative; width: 1200px; height: 1000px; }

  .card {
    position: absolute;
    width: 540px; height: 310px;
    border-radius: 14px;
    overflow: hidden;
  }

  /* Rear of card */
  .card-back {
    left: 70px; top: 150px;
    background: var(--card-black);
    clip-path: polygon(0 0, 90% 0, 100% 16%, 100% 100%, 0 100%);
  }
  .card-back .accent-bar {
    position: absolute; left: 0; top: 60px;
    width: 9px; height: 64px; background: var(--sky);
  }
  .card-back .wordmark {
    position: absolute; left: 60px; top: 58px;
    font-size: 42px; font-weight: 300; letter-spacing: 3px;
    color: var(--silver); white-space: nowrap;
  }
  .card-back .tagline {
    position: absolute; left: 62px; top: 110px;
    font-size: 17px; font-weight: 400; color: var(--silver);
  }
  .card-back .web-url {
    position: absolute; left: 62px; bottom: 40px;
    font-size: 14px; font-weight: 400; letter-spacing: 0.5px;
    color: var(--silver-soft);
  }

  /* Front of card */
  .card-front {
    left: 590px; top: 520px;
    background: var(--paper-white);
    clip-path: polygon(0 0, 100% 0, 100% 100%, 12% 100%, 0 80%);
  }
  .card-front .contact-band {
    position: absolute; left: 0; top: 42px;
    width: 100%; height: 84px;
    background: var(--band-black);
  }
  .card-front .sky-rule {
    position: absolute; left: 0; top: 130px;
    width: 100%; height: 3px; background: var(--sky);
  }
  .person-name {
    position: absolute; left: 40px; top: 20px;
    font-size: 20px; font-weight: 700; color: var(--paper-white);
  }
  .person-title {
    position: absolute; left: 40px; top: 47px;
    font-size: 15px; font-weight: 400; color: var(--silver-soft);
  }
  .direct-lines {
    position: absolute; right: 36px; top: 20px;
    font-size: 13px; line-height: 19px; color: var(--silver-soft);
  }
  .card-front .wordmark {
    position: absolute; left: 56px; top: 214px;
    font-size: 30px; font-weight: 400; letter-spacing: 2px;
    color: var(--ink); white-space: nowrap;
  }
  .card-front .tagline {
    position: absolute; left: 58px; top: 254px;
    font-size: 13px; color: var(--ink);
  }
  .company-address {
    position: absolute; left: 300px; top: 160px;
    font-size: 13px; line-height: 18px; color: var(--ink-soft);
    font-style: normal; white-space: nowrap;
  }
  .company-address .company-name { font-weight: 700; color: var(--ink); margin-bottom: 4px; }
  .company-address .email-line { margin-top: 8px; }
</style>
</head>
<body>
<main class="canvas">
  <section class="card card-back" aria-label="Back of card">
    <span class="accent-bar"></span>
    <div class="wordmark">LUMO RIDES</div>
    <div class="tagline">Arrive Polished.</div>
    <div class="web-url">www.lumorides.example</div>
  </section>

  <section class="card card-front" aria-label="Front of card">
    <div class="contact-band">
      <div class="person-name">Baraka Kilonzo</div>
      <div class="person-title">Managing Director</div>
      <div class="direct-lines">
        +255 (0) 712 904618<br>
        sales@lumorides.example
      </div>
    </div>
    <span class="sky-rule"></span>
    <div class="wordmark">LUMO RIDES</div>
    <div class="tagline">Arrive Polished.</div>
    <address class="company-address">
      <div class="company-name">Lumo Rides Limited</div>
      P.O. Box 58104<br>
      Dar es Salaam, Tanzania
      <div class="email-line">E : chauffeur@lumorides.example</div>
    </address>
  </section>
</main>
</body>
</html>
```